Business card for Chiropractic clinics needs reworked / redesigned

The business card in attachment was designed 10 years ago. It is in need of an update.
We have 2 clinics:
VELDHOVE KLINIEK & VELDHOVE KLINIEK NOORD
Only one address needs to be on the card for doctors that only work in one clinic and two addresses need to be on the card for the doctors that work in both clinics.

Target Market(s)

patients/referrers

Industry/Entity Type

Medical

Contact Information for Business Card

Logo (in full or zoomed-in)
Clinic Name
Doctor name and title
clinic address, website, tel, email

Font styles to use
Sans Serif

Colors

Designer to choose colors to be used in the design.

Requirements
Must have
• Good contrast/readability
• We like modern minimalistic designs
• The Bcard needs to project our very high standard of proficiency/professionalism
Should not have
• Not curly
• Not to much colours

```html
<!DOCTYPE html>
<html lang="nl">
<head>
<meta charset="utf-8">
<title>Veldhove Kliniek – business card</title>
<link rel="stylesheet" href="https://fonts.googleapis.com/css2?family=Lato:wght@400;700;900&display=swap">
<style>
  :root {
    --green: #5df23a;
    --green-soft: #8ef774;
    --ink: #1d2020;
    --paper: #ffffff;
    --paper-soft: #eef1ee;
    --stage: #1e1f21;
  }
  * { box-sizing: border-box; margin: 0; padding: 0; }
  html, body { width: 1200px; height: 1200px; overflow: hidden; }
  body {
    background: var(--stage);
    font-family: "Lato", sans-serif;
    position: relative;
  }
  .card {
    position: absolute;
    left: 160px;
    width: 880px;
    height: 500px;
    overflow: hidden;
  }

  /* Front */
  .card--front { top: 70px; background: var(--green); }
  .front-mark {
    position: absolute;
    left: 30px;
    top: 120px;
    width: 300px;
    height: 330px;
    border-radius: 18px;
    background: linear-gradient(160deg, var(--green-soft), var(--green));
  }
  .front-name {
    position: absolute;
    left: 350px;
    top: 250px;
    color: var(--paper);
    font-weight: 700;
    font-size: 48px;
    letter-spacing: 1px;
    white-space: nowrap;
  }

  /* Back */
  .card--back { top: 630px; background: var(--paper); }
  .back-mark {
    position: absolute;
    left: 50px;
    top: 90px;
    width: 220px;
    height: 270px;
    border-radius: 16px;
    background: linear-gradient(160deg, var(--paper-soft), #dfe4df);
  }
  .back-brand {
    position: absolute;
    left: 285px;
    top: 268px;
    color: var(--ink);
    font-weight: 700;
    font-size: 30px;
    line-height: 1.1;
    letter-spacing: .5px;
  }
  .divider {
    position: absolute;
    left: 500px;
    top: 135px;
    width: 2px;
    height: 210px;
    background: linear-gradient(var(--paper), var(--green) 40%, var(--ink));
  }
  .person { position: absolute; left: 520px; top: 44px; right: 30px; }
  .person-name { color: var(--green); font-weight: 900; font-size: 22px; white-space: nowrap; }
  .person-role { color: var(--ink); font-size: 16px; margin-top: 5px; letter-spacing: .5px; }
  .person-mobile { color: var(--green); font-size: 16px; margin-top: 6px; display: flex; align-items: center; gap: 8px; }
  .contact { position: absolute; left: 540px; top: 200px; list-style: none; }
  .contact li {
    display: flex; align-items: center; gap: 12px;
    color: var(--ink); font-size: 18px; height: 33px;
    white-space: nowrap;
  }
  .contact svg { width: 20px; height: 20px; flex: none; }
  .band {
    position: absolute; left: 0; right: 0; bottom: 0; height: 56px;
    background: var(--green);
  }
  .band-rise {
    position: absolute; left: 520px; right: 0; bottom: 0; height: 92px;
    background: var(--green); border-top-left-radius: 26px;
  }
  .band-tab {
    position: absolute; left: 560px; right: 0; bottom: 0; height: 70px;
    background: var(--ink); border-top-left-radius: 26px;
  }
</style>
</head>
<body>
  <section class="card card--front" aria-label="Card front">
    <div class="front-mark" role="img" aria-label="Clinic logo mark"></div>
    <div class="front-name">VELDHOVE KLINIEK</div>
  </section>

  <section class="card card--back" aria-label="Card back">
    <div class="back-mark" role="img" aria-label="Clinic logo mark"></div>
    <div class="back-brand">VELDHOVE<br>KLINIEK</div>

    <div class="person">
      <div class="person-name">Pieter VANDENBROUCKE D.C.</div>
      <div class="person-role">CHIROPRACTOR</div>
      <div class="person-mobile">
        <svg width="12" height="18" viewBox="0 0 12 18"><rect x="1" y="1" width="10" height="16" rx="2" fill="none" stroke="currentColor" stroke-width="1.6"/><circle cx="6" cy="14" r="1" fill="currentColor"/></svg>
        0470 12 34 56
      </div>
    </div>

    <div class="divider"></div>

    <ul class="contact">
      <li><svg viewBox="0 0 20 20"><path d="M10 2a5 5 0 0 0-5 5c0 4 5 9 5 9s5-5 5-9a5 5 0 0 0-5-5z" fill="var(--green)"/><circle cx="10" cy="7" r="2" fill="#fff"/><ellipse cx="10" cy="18" rx="6" ry="1.4" fill="none" stroke="var(--green)" stroke-width="1.2"/></svg>Kouterstraat 48, 9050 Veldhove</li>
      <li><svg viewBox="0 0 20 20"><rect x="1" y="2" width="18" height="16" rx="3" fill="var(--green)"/><path d="M7 5l2 3-1.5 1.2a7 7 0 0 0 3.3 3.3L12 11l3 2-1 2c-5 0-9-4-9-9z" fill="#fff"/></svg>+32 (0)9 555 01 23</li>
      <li><svg viewBox="0 0 20 20"><rect x="1" y="4" width="18" height="12" fill="var(--green)"/><path d="M1 4l9 7 9-7" fill="none" stroke="#fff" stroke-width="1.5"/></svg>info@veldhovekliniek.be</li>
      <li><svg viewBox="0 0 20 20" fill="none" stroke="var(--green)" stroke-width="1.4"><circle cx="10" cy="10" r="8"/><ellipse cx="10" cy="10" rx="3.5" ry="8"/><path d="M2 10h16M3.5 6h13M3.5 14h13"/></svg>www.veldhovekliniek.be</li>
    </ul>

    <div class="band"></div>
    <div class="band-rise"></div>
    <div class="band-tab"></div>
  </section>
</body>
</html>
```